Product Label Design

Need a product design for our Epsom salt product, needs to have a luxurious simple feel to it. The picture attached is our brand and wordage on it, the bag we think should be a stand up bag that should be offwhite/creme color. The other picture are products that we like. We updated the packaging to be a Kraft tube box, please see the attached photo for dimensions.

```html
<!DOCTYPE html>
<html lang="en">
<head>
<meta charset="utf-8">
<title>Epsom Salt Label</title>
<link rel="stylesheet" href="https://fonts.googleapis.com/css2?family=Montserrat:wght@500;600;700&family=Playfair+Display:wght@400;500&display=swap">
<style>
  :root {
    --stage: #eee3d9;
    --label: #fcf1e9;
    --gold: #a98a5f;
    --gold-soft: #d7c2a0;
    --ink: #5b4b3b;
    --ink-dark: #2e2620;
    --rule: #8f7a62;
    --wave-warm: #f6dcb4;
    --wave-blush: #f7e3d6;
  }
  * { margin: 0; padding: 0; box-sizing: border-box; }
  html, body { width: 1200px; height: 921px; overflow: hidden; background: var(--stage); }
  .label {
    position: absolute; left: 315px; top: 0; width: 570px; height: 921px;
    background: var(--label); overflow: hidden;
  }
  .brand {
    position: absolute; top: 160px; left: 0; width: 100%;
    display: flex; align-items: center; justify-content: center; gap: 12px;
    font-family: "Playfair Display", serif; font-size: 27px; color: var(--gold);
    letter-spacing: 0.5px;
  }
  .brand-dot { width: 20px; height: 20px; border-radius: 50%; background: var(--gold); }
  .product-name {
    position: absolute; top: 300px; left: 0; width: 100%; text-align: center;
    font-family: "Playfair Display", serif; font-weight: 500; font-size: 70px;
    color: var(--gold); line-height: 1;
  }
  .title-rule {
    position: absolute; top: 394px; left: 116px; width: 338px; height: 2px; background: var(--ink);
  }
  .tagline {
    position: absolute; top: 404px; left: 0; width: 100%; text-align: center;
    font-family: "Montserrat", sans-serif; font-weight: 600; font-size: 16px;
    letter-spacing: 2px; color: var(--ink);
  }
  .benefits {
    position: absolute; top: 497px; left: 187px; width: 196px; list-style: none;
    border-top: 1.5px solid var(--rule);
  }
  .benefits li {
    font-family: "Playfair Display", serif; font-size: 23px; color: var(--ink-dark);
    text-align: center; height: 54px; line-height: 54px;
    border-bottom: 1.5px solid var(--gold-soft);
    white-space: nowrap;
  }
  .benefits li:last-child { border-bottom: none; }
  .benefits li::before { content: "• "; color: var(--gold); }
  .leaf-area {
    position: absolute; top: 470px; left: 300px; width: 270px; height: 230px;
    background: radial-gradient(ellipse at 60% 50%, rgba(240,205,185,0.55), rgba(252,241,233,0) 70%);
  }
  .wave-area {
    position: absolute; left: 0; bottom: 0; width: 100%; height: 290px;
    background: linear-gradient(170deg, rgba(252,241,233,0) 10%, var(--wave-warm) 45%, var(--wave-blush) 75%, var(--label) 100%);
  }
  .net-weight {
    position: absolute; top: 856px; right: 18px;
    font-family: "Montserrat", sans-serif; font-weight: 700; font-size: 17px; color: var(--ink-dark);
  }
</style>
</head>
<body>
  <main class="label">
    <div class="leaf-area" role="img" aria-label="Soft botanical leaf sprig decoration"></div>
    <div class="wave-area" role="img" aria-label="Flowing cream and gold wave pattern"></div>
    <div class="brand"><span class="brand-dot"></span><span>gentle meadow</span></div>
    <h1 class="product-name">Epsom Salt</h1>
    <div class="title-rule"></div>
    <p class="tagline">Relax • Restore • Rejuvenate</p>
    <ul class="benefits">
      <li>Muscle Relaxation</li>
      <li>Stress Relief</li>
      <li>Pure &amp; Natural</li>
    </ul>
    <p class="net-weight">NET WT.3LBS (1360G)</p>
  </main>
</body>
</html>
```